IT services company needs a business card designed

-2 sided business card.-Front is going to be the logo raised (3D floating effect) on a black background. Make the logos spider web shiny silver and keep the spider the same design. -Back needs to have the following information:Darrel Sotho, Managing Partner, Cell: 738-402-1954, Website: Plankhorn.com, Email: Darrel@Plankhorn.com
Target Market(s)
IT Services
Industry/Entity Type
It Company
Contact Information for Business Card
-2 sided business card.
-Front is going to be the logo raised (3D floating effect) on a black background. Make the logos spider web shiny silver and keep the spider the same design.
-Back needs to have the following information:
Darrel Sotho, Managing Partner, Cell: 738-402-1954, Website: Plankhorn.com, Email: Darrel@Plankhorn.com

```html
<!DOCTYPE html>
<html lang="en">
<head>
<meta charset="utf-8">
<title>Plankhorn Business Card</title>
<link href="https://fonts.googleapis.com/css2?family=Montserrat:wght@400;600;700&family=Open+Sans:wght@400&display=swap" rel="stylesheet">
<style>
  :root {
    --page: #e3e3e3;
    --card-black: #050505;
    --card-charcoal: #1c1c1c;
    --card-white: #f7f7f7;
    --accent-blue: #1a96dc;
    --band-gray: #6f6f70;
    --silver: #cfcfcf;
    --ink: #2a2a2a;
  }
  * { margin: 0; padding: 0; box-sizing: border-box; }
  html, body { width: 1200px; height: 1200px; overflow: hidden; }
  body {
    background: var(--page);
    font-family: "Open Sans", sans-serif;
    position: relative;
  }
  .card {
    position: absolute;
    left: 250px;
    width: 700px;
    height: 400px;
    overflow: hidden;
    box-shadow: 0 14px 30px rgba(0,0,0,0.18);
  }
  .card--front {
    top: 150px;
    background: radial-gradient(circle at 45% 40%, var(--card-charcoal) 0%, var(--card-black) 65%);
  }
  .card--back {
    top: 650px;
    background: var(--card-white);
  }
  .band-gray {
    position: absolute; left: 0; bottom: 0;
    width: 56%; height: 14px;
    background: var(--band-gray);
  }
  .band-blue {
    position: absolute; right: 0; bottom: 14px;
    width: 44%; height: 16px;
    background: var(--accent-blue);
  }
  .band-blue::after {
    content: ""; position: absolute; left: 0; right: 0; bottom: -14px; height: 14px;
    background: var(--card-white);
  }
  .card--front .band-blue::after { background: var(--card-black); }

  .front-logo {
    position: absolute; left: 50%; top: 70px; transform: translateX(-50%);
    display: flex; flex-direction: column; align-items: center; gap: 18px;
  }
  .web-art--silver {
    width: 170px; height: 150px; border-radius: 50%;
    background: radial-gradient(circle, #eeeeee 0%, #9a9a9a 45%, rgba(60,60,60,0.3) 75%, transparent 100%);
  }
  .wordmark {
    font-family: "Montserrat", sans-serif;
    font-weight: 400;
    letter-spacing: 3px;
  }
  .card--front .wordmark { color: var(--silver); font-size: 40px; }

  .back-logo {
    position: absolute; left: 70px; top: 130px;
    display: flex; flex-direction: column; align-items: center; gap: 12px;
  }
  .web-art--blue {
    width: 130px; height: 115px; border-radius: 50%;
    background: radial-gradient(circle, #1a96dc 0%, #7cc0e8 45%, rgba(200,200,200,0.5) 75%, transparent 100%);
  }
  .card--back .wordmark { color: var(--ink); font-size: 28px; }

  .contact-block {
    position: absolute; left: 355px; top: 70px;
  }
  .contact-name {
    font-family: "Montserrat", sans-serif; font-weight: 700;
    color: var(--accent-blue); font-size: 34px; line-height: 1.1;
  }
  .contact-role {
    font-size: 19px; color: var(--ink); margin-bottom: 26px;
  }
  .contact-list { list-style: none; }
  .contact-list li {
    display: flex; align-items: center; gap: 12px;
    font-size: 17px; color: var(--ink); margin-bottom: 10px;
  }
  .icon { width: 20px; height: 20px; flex: none; }
</style>
</head>
<body>
  <section class="card card--front">
    <div class="front-logo">
      <div class="web-art--silver" role="img" aria-label="Shiny silver spider-web emblem"></div>
      <div class="wordmark">PLANKHORN</div>
    </div>
    <div class="band-gray"></div>
    <div class="band-blue"></div>
  </section>

  <section class="card card--back">
    <div class="back-logo">
      <div class="web-art--blue" role="img" aria-label="Blue and silver spider-web emblem"></div>
      <div class="wordmark">PLANKHORN</div>
    </div>
    <div class="contact-block">
      <div class="contact-name">Darrel Sotho</div>
      <div class="contact-role">Managing Partner</div>
      <ul class="contact-list">
        <li>
          <svg class="icon" viewBox="0 0 20 20"><circle cx="10" cy="10" r="10" fill="#2a2a2a"/><path d="M6.5 5.5l2 0 .8 2.4-1.3 1c.6 1.3 1.5 2.2 2.8 2.8l1-1.3 2.4.8 0 2c-4.5.2-7.9-3.2-7.7-7.7z" fill="#fff"/></svg>
          738-402-1954
        </li>
        <li>
          <svg class="icon" viewBox="0 0 20 20"><circle cx="10" cy="10" r="10" fill="#2a2a2a"/><circle cx="10" cy="10" r="5.5" fill="none" stroke="#fff" stroke-width="1.2"/><path d="M4.5 10h11M10 4.5c-2.5 3-2.5 8 0 11M10 4.5c2.5 3 2.5 8 0 11" fill="none" stroke="#fff" stroke-width="1"/></svg>
          www.plankhorn.com
        </li>
        <li>
          <svg class="icon" viewBox="0 0 20 20"><circle cx="10" cy="10" r="10" fill="#2a2a2a"/><rect x="5" y="6.5" width="10" height="7" fill="none" stroke="#fff" stroke-width="1.2"/><path d="M5 6.5l5 4 5-4" fill="none" stroke="#fff" stroke-width="1.2"/></svg>
          Darrel@Plankhorn.com
        </li>
      </ul>
    </div>
    <div class="band-gray"></div>
    <div class="band-blue"></div>
  </section>
</body>
</html>
```